Business Card Design

Hi we are an MMA and fitness gym, we would like a design similar to the themes in the logo provided and with all the information on it as well.
Updates

1. The phone number is 0455 612 907
2. The address is 18 Calloway street

Hi some of the designs have the wrong phone number the correct number is 0417 583 640

the correct address is 18 Calloway Street 

Industry/Entity Type

Fitness

Contact Information for Business Card

Danielle Fairow
Club Manager
0417 583 640
18 Calloway Street Wynnum Central
Qld 4178
gym@ironvalemma.com.au
www.ironvalemma.com.au

MMA, Boxing, Muay Thai, Kids MMA, BlazeRun group fitness

```html
<!DOCTYPE html>
<html lang="en">
<head>
<meta charset="utf-8">
<title>Ironvale MMA Gym – Business Card</title>
<link rel="stylesheet" href="https://fonts.googleapis.com/css2?family=Arimo:wght@700&family=Roboto+Condensed:wght@300;400&display=swap">
<style>
  :root {
    --stage: #1c2422;
    --card-front-dark: #141414;
    --card-front-mid: #3a3a3a;
    --card-back: #1b1b1b;
    --card-back-light: #2c2c2c;
    --text-light: #ffffff;
    --text-soft: #e4e4e4;
    --text-muted: #c9c9c9;
    --brand-grey: #d8d8d8;
  }
  * { margin: 0; padding: 0; box-sizing: border-box; }
  html, body { width: 1200px; height: 1045px; overflow: hidden; }
  body {
    position: relative;
    background: var(--stage);
    font-family: "Roboto Condensed", "Arial Narrow", sans-serif;
    color: var(--text-light);
  }

  .card { position: absolute; overflow: hidden; box-shadow: 0 6px 18px rgba(0,0,0,.55); }

  /* Front side */
  .card-front {
    left: 215px; top: 115px; width: 640px; height: 347px;
    background:
      repeating-linear-gradient(180deg, rgba(255,255,255,.025) 0 1px, transparent 1px 3px),
      linear-gradient(90deg, var(--card-front-dark) 0%, var(--card-front-mid) 55%, #555 75%, var(--card-front-dark) 100%);
  }
  .card-front .brand {
    position: absolute; left: 0; right: 0; top: 120px;
    text-align: center;
  }
  .card-front .web {
    position: absolute; left: 0; right: 0; top: 266px;
    text-align: center; font-size: 15px; color: var(--text-muted);
  }
  .card-front .services {
    position: absolute; left: 0; right: 0; top: 296px;
    text-align: center; font-size: 24px; font-weight: 300; color: var(--text-muted);
  }

  /* Brand name stand-in */
  .brand-name {
    display: inline-flex; align-items: center; gap: 14px;
    font-family: "Roboto Condensed", "Arial Narrow", sans-serif;
    font-weight: 400; color: var(--brand-grey);
    text-transform: uppercase; letter-spacing: 2px;
  }
  .brand-mark { display: inline-block; border-radius: 50%; background: var(--brand-grey); }
  .card-front .brand-name { font-size: 46px; }
  .card-front .brand-mark { width: 28px; height: 28px; }

  /* Back side */
  .card-back {
    left: 410px; top: 503px; width: 702px; height: 382px;
    background: radial-gradient(ellipse at 65% 35%, var(--card-back-light) 0%, var(--card-back) 70%);
  }
  .card-back .texture {
    position: absolute; inset: 0;
    background: linear-gradient(160deg, rgba(255,255,255,.04), rgba(0,0,0,.15));
  }
  .contact { position: absolute; left: 28px; top: 95px; }
  .contact .name {
    font-family: "Arimo", Arial, sans-serif; font-weight: 700;
    font-size: 29px; line-height: 1; color: var(--text-light);
  }
  .contact .role { margin-top: 12px; font-size: 18px; color: var(--text-soft); }
  .contact .details { list-style: none; margin-top: 34px; font-size: 19px; color: var(--text-soft); }
  .contact .details li { height: 31px; line-height: 22px; }
  .card-back .brand {
    position: absolute; left: 355px; top: 175px; width: 330px; text-align: center;
  }
  .card-back .brand-name { font-size: 40px; }
  .card-back .brand-mark { width: 24px; height: 24px; }
  .card-back .services {
    position: absolute; left: 28px; top: 330px;
    font-size: 27px; color: var(--text-light);
  }
</style>
</head>
<body>

  <section class="card card-front" aria-label="Business card front">
    <div class="brand">
      <span class="brand-name"><span class="brand-mark"></span>Ironvale MMA Gym</span>
    </div>
    <p class="web">www.ironvalemma.com.au</p>
    <p class="services">MMA, Boxing, Muay Thai, Kids MMA, BlazeRun group fitness</p>
  </section>

  <section class="card card-back" aria-label="Business card back">
    <div class="texture" role="img" aria-label="Dark diamond plate metal texture"></div>
    <div class="contact">
      <h1 class="name">Danielle Fairow</h1>
      <p class="role">Club Manager</p>
      <ul class="details">
        <li>18 Calloway st</li>
        <li>gym@ironvalemma.com.au</li>
        <li>0417 583 640</li>
        <li>www.ironvalemma.com.au</li>
      </ul>
    </div>
    <div class="brand">
      <span class="brand-name"><span class="brand-mark"></span>Ironvale MMA Gym</span>
    </div>
    <p class="services">MMA, Boxing, Muay Thai, Kids MMA, BlazeRun group fitness</p>
  </section>

</body>
</html>
```